Business Card Design Project

We need a simple business card design that uses our current logo.
We need to have the current logo put into a high res format.
We need to have 1 card made with contact information.
We will supply the information for the 4 employees.
Industry/Entity Type
Business
Requirements
Must have
- The contact information is as follows:
Paul Vardenko
Producer/CEO
c. 949-555-0148
f. 650-555-0193
paulv@lanternyardstudio.example
Mel Trosgaard, CFO
c. 949-555-0172
f. 650-555-0193
melt@lanternyardstudio.example
Paul Brenneky, PR
c. 267-555-0126
f. 650-555-0193
pbrenneky@lanternyardstudio.example
Dale Furnow, Producer
c. 949-555-0164
f. 650-555-0193
dalef@lanternyardstudio.example
The address for all cards is:
318 W Calle Norvista #2715, San Clemente, CA 92631

```html
<!DOCTYPE html>
<html lang="en">
<head>
<meta charset="utf-8">
<title>Lantern Yard Studio – Business Card</title>
<link rel="stylesheet" href="https://fonts.googleapis.com/css2?family=Arvo:wght@700&family=Arimo:wght@400&display=swap">
<style>
  :root {
    --page-bg: #e9e6e1;
    --card-blue: #6e9fcd;
    --card-shade: #4d7aa6;
    --card-edge: #0b0b0c;
    --ink-light: #ffffff;
    --ink-dark: #0d1b2a;
  }
  * { box-sizing: border-box; margin: 0; padding: 0; }
  html, body {
    width: 1200px; height: 740px; overflow: hidden;
    background: var(--page-bg);
  }
  .sheet {
    position: relative; width: 1200px; height: 740px;
    display: flex; align-items: center; justify-content: center; gap: 60px;
  }
  .card {
    position: relative; width: 540px; height: 310px;
    background: var(--card-blue);
    border: 10px solid var(--card-edge);
    overflow: hidden;
  }
  /* contact side */
  .card-contact .watermark-name {
    position: absolute; left: 0; right: 0; top: 118px;
    text-align: center;
    font-family: "Arvo", Georgia, serif; font-weight: 700;
    font-size: 36px;
    color: var(--card-shade); opacity: .45;
    white-space: nowrap;
  }
  .identity {
    position: absolute; left: 14px; top: 192px; width: 202px; text-align: right;
  }
  .identity .person-name {
    font-family: "Arvo", Georgia, serif; font-weight: 700;
    font-size: 21px; color: var(--ink-light); line-height: 1.1;
    white-space: nowrap;
  }
  .identity .person-role {
    margin-top: 6px;
    font-family: "Arimo", Arial, sans-serif; font-size: 14px; color: var(--ink-light);
  }
  .divider {
    position: absolute; left: 228px; top: 60px; width: 2px; height: 190px;
    background: var(--ink-light);
  }
  .contact-list {
    position: absolute; left: 244px; top: 58px; list-style: none;
    font-family: "Arimo", Arial, sans-serif; font-size: 14px; color: var(--ink-light);
  }
  .contact-list li {
    display: flex; align-items: flex-start; gap: 10px; margin-bottom: 18px; line-height: 1.3;
    white-space: nowrap;
  }
  .contact-list svg { flex: none; width: 20px; height: 18px; margin-top: 1px; }
  /* logo side */
  .card-logo { display: flex; align-items: center; justify-content: center; }
  .company-name {
    font-family: "Arvo", Georgia, serif; font-weight: 700;
    font-size: 36px; color: var(--ink-dark);
    white-space: nowrap;
  }
</style>
</head>
<body>
  <main class="sheet">
    <section class="card card-contact" aria-label="Contact side">
      <div class="watermark-name" aria-hidden="true">LANTERN YARD STUDIO</div>
      <div class="identity">
        <p class="person-name">Paul Vardenko</p>
        <p class="person-role">Producer/CEO</p>
      </div>
      <div class="divider"></div>
      <ul class="contact-list">
        <li>
          <svg viewBox="0 0 20 18" aria-hidden="true"><path d="M10 1 L1 9 H4 V17 H8 V12 H12 V17 H16 V9 H19 Z" fill="#fff"/></svg>
          <span>318 W Calle Norvista #2715,<br>San Clemente, CA 92631</span>
        </li>
        <li>
          <svg viewBox="0 0 20 18" aria-hidden="true"><rect x="1" y="0" width="18" height="18" rx="3" fill="#fff"/><path d="M6 4 C5 8 9 13 14 14 L15 12 L12.5 10.5 L11.5 11.5 C10 11 8 9 7.5 7.5 L8.5 6.5 L7.5 4 Z" fill="#6e9fcd"/></svg>
          <span>949-555-0148</span>
        </li>
        <li>
          <svg viewBox="0 0 20 18" aria-hidden="true"><rect x="1" y="6" width="18" height="11" rx="1.5" fill="#fff"/><rect x="5" y="1" width="10" height="6" fill="#fff"/><rect x="5" y="10" width="10" height="1.5" fill="#6e9fcd"/><rect x="5" y="13" width="10" height="1.5" fill="#6e9fcd"/></svg>
          <span>650-555-0193</span>
        </li>
        <li>
          <svg viewBox="0 0 20 18" aria-hidden="true"><rect x="1" y="3" width="18" height="12" fill="#fff"/><path d="M1 3 L10 10 L19 3" fill="none" stroke="#6e9fcd" stroke-width="1.5"/></svg>
          <span>paulv@lanternyardstudio.example</span>
        </li>
      </ul>
    </section>

    <section class="card card-logo" aria-label="Logo side">
      <p class="company-name">LANTERN YARD STUDIO</p>
    </section>
  </main>
</body>
</html>
```